Postcard Design Desert Hot Springs Land Sale - Solicit new sellers of land

I sell land in Desert Hot Springs CA. My company is Q7 Estates. I am looking for a great oversize postcard that shows my land listing and also solicits new business. I would like the postcard to serve as a template for many different listings. I also want a flyer designed to match the feeling and look of the postcard.

Target Market(s)

Land owners that are considering selling their land

Industry/Entity Type

Real Estate Development

Colors
3276b5

Requirements
Must have
• Professional look and feel. Be an example template for a flyer to have you design

```html
<!DOCTYPE html>
<html lang="en">
<head>
<meta charset="utf-8">
<title>Q7 Estates – Land Listing Flyer</title>
<link href="https://fonts.googleapis.com/css2?family=Source+Sans+3:ital,wght@0,400;0,600;0,700;1,700&display=swap" rel="stylesheet">
<style>
  :root {
    --brand-blue: #3276b5;
    --deep-blue: #123f6e;
    --ink: #333a42;
    --muted: #4a4f55;
    --panel-grey: #d9dadc;
    --content-grey: #efeff0;
    --white: #ffffff;
    --ribbon-red: #d42a22;
    --map-sand: #b9b2a6;
    --map-shadow: #8f897e;
  }
  * { box-sizing: border-box; margin: 0; padding: 0; }
  html, body { width: 982px; height: 1200px; overflow: hidden; background: var(--white); }
  body { font-family: "Source Sans 3", sans-serif; color: var(--ink); }
  .flyer { position: relative; width: 982px; height: 1200px; }

  .masthead { position: absolute; top: 0; left: 0; width: 982px; height: 144px; background: var(--white); }
  .brand { position: absolute; left: 40px; top: 34px; }
  .brand-name { font-size: 48px; font-weight: 400; color: var(--ink); letter-spacing: 3px; line-height: 1; }
  .brand-tagline { margin-top: 10px; font-size: 13px; letter-spacing: 3.2px; color: var(--ink); text-transform: uppercase; }
  .office { position: absolute; left: 742px; top: 38px; font-size: 17px; line-height: 24px; color: var(--muted); }

  .site-map { position: absolute; top: 144px; left: 0; width: 982px; height: 372px;
    background: linear-gradient(120deg, var(--map-sand) 0%, #c6c0b4 45%, var(--map-shadow) 100%); overflow: hidden; }
  .site-map .divider { position: absolute; left: 0; top: 297px; width: 100%; height: 2px; background: rgba(255,255,255,.9); }
  .ribbon { position: absolute; right: 0; top: 0; }

  .price-band { position: absolute; top: 516px; left: 0; width: 982px; height: 135px;
    background: linear-gradient(90deg, var(--brand-blue) 0%, #24609c 55%, var(--deep-blue) 100%); color: var(--white); }
  .listing-summary { position: absolute; left: 54px; top: 33px; font-size: 25px; line-height: 32px; }
  .listing-price { position: absolute; left: 590px; top: 42px; font-size: 45px; font-weight: 700; letter-spacing: .5px; }

  .agent-panel { position: absolute; top: 651px; left: 0; width: 366px; height: 509px; background: var(--panel-grey); }
  .agent-photo { position: absolute; left: 56px; top: 62px; width: 204px; height: 236px;
    border-top: 3px solid #7d8086; border-left: 3px solid #7d8086; padding: 6px; }
  .agent-photo div { width: 100%; height: 100%; background: linear-gradient(180deg, #e4e6e8 0%, #c9ccd1 55%, #2b2f36 100%); }
  .agent-name { position: absolute; left: 60px; top: 312px; font-size: 27px; color: var(--brand-blue); }
  .agent-title { position: absolute; left: 60px; top: 344px; font-size: 20px; color: var(--ink); }
  .agent-contact { position: absolute; left: 60px; top: 386px; font-size: 16px; line-height: 22px; color: var(--ink); }

  .details { position: absolute; top: 651px; left: 366px; width: 616px; height: 509px; background: var(--content-grey); }
  .details-heading { position: absolute; left: 44px; top: 60px; font-size: 31px; font-weight: 700; font-style: italic;
    color: #1d5a9b; letter-spacing: .5px; }
  .features { position: absolute; left: 45px; top: 117px; list-style: none; }
  .features li { font-size: 30px; line-height: 44px; color: var(--ink); padding-left: 20px; position: relative; }
  .features li::before { content: ""; position: absolute; left: 0; top: 18px; width: 9px; height: 9px; background: #3c4148; }
  .cta { position: absolute; left: 0; width: 100%; top: 390px; text-align: center; color: var(--brand-blue); }
  .cta-line { font-size: 24px; }
  .cta-line strong { font-weight: 700; }
  .cta-phone { margin-top: 6px; font-size: 29px; font-weight: 700; display: inline-flex; align-items: center; gap: 12px; }

  .footer-bar { position: absolute; left: 0; top: 1160px; width: 982px; height: 40px;
    background: linear-gradient(90deg, var(--brand-blue), var(--deep-blue)); }
</style>
</head>
<body>
<main class="flyer">
  <header class="masthead">
    <div class="brand">
      <div class="brand-name">Q7 Estates</div>
      <div class="brand-tagline">Selling Palm Springs Area Real Estate</div>
    </div>
    <address class="office" style="font-style:normal">
      212 Sandstone Way<br>Palm Desert CA 92260<br>Cell: 760 555 0142
    </address>
  </header>

  <section class="site-map" role="img" aria-label="Aerial map of the 16-acre desert parcel with surrounding roads and lot lines">
    <div class="divider"></div>
    <svg class="ribbon" width="210" height="170" viewBox="0 0 210 170" aria-hidden="true">
      <polygon points="0,0 48,0 210,140 210,170" fill="#8f1a15"/>
      <polygon points="10,0 58,0 210,128 210,160" fill="var(--ribbon-red)"/>
      <text x="0" y="0" transform="translate(88,40) rotate(41)" fill="#fff" font-family="Source Sans 3, sans-serif" font-weight="700" font-size="30">FOR SALE!</text>
    </svg>
  </section>

  <section class="price-band">
    <p class="listing-summary">16 Acres Gross | Zoned for Marijuana<br>Cultivation Desert Hot Springs, CA</p>
    <p class="listing-price">$2,200,000.00</p>
  </section>

  <aside class="agent-panel">
    <div class="agent-photo"><div role="img" aria-label="Portrait photo of the broker"></div></div>
    <p class="agent-name">Daniel Marlow</p>
    <p class="agent-title">Broker | Q7 Estates</p>
    <p class="agent-contact">Cell: 760 555 0142<br>Fax: 866 555 0187<br>q7estates@mailbox.com</p>
  </aside>

  <section class="details">
    <h2 class="details-heading">Zoned for Marijuana Cultivation</h2>
    <ul class="features">
      <li>APN 612 340 00</li>
      <li>16 acres gross zoned Light Ind</li>
      <li>Utilities available</li>
      <li>Paved road fronts the prop</li>
      <li>Large scale cultivation encouraged</li>
      <li>30 day escrow</li>
    </ul>
    <div class="cta">
      <p class="cta-line"><strong>Is your property in this zone?</strong> Call or Text</p>
      <p class="cta-phone">
        <svg width="32" height="32" viewBox="0 0 32 32" aria-hidden="true">
          <circle cx="16" cy="16" r="14" fill="none" stroke="currentColor" stroke-width="2.5"/>
          <path d="M11 8.5l3 3.2-1.8 2.2c1 2.3 2.8 4.1 5.1 5.1l2.2-1.8 3.2 3-1.9 3c-5.6-.5-11-5.9-11.5-11.5z" fill="currentColor"/>
        </svg>
        760 555 0142
      </p>
    </div>
  </section>

  <footer class="footer-bar"></footer>
</main>
</body>
</html>
```